Brand new letterhead, business card, email signature etc.

We are a financial company in London, UK. Our website is www.quorvane.com. We're wanting a complete remodel of the company colours, letter head, business cards, email signatures, etc. Looking to keep the same font for the company name. I have upload a colour palette that we want to work with. We're looking for company letterhead for outgoing letters/ correspondence, letterhead for internal documentation, email signatures, e-letters. etc. Ultimately we will redesign the entire website also. It is important that our clients get a strong, secure, warm, trustworthy, solid feeling and first impression.
Updates

Designs look the same

Target Market(s)

Institutional investors, (ultra) high net worth individuals

Industry/Entity Type

Finance, Invesments banking.

Font styles to use
Other font styles liked:
• Current font is "Champagne & Limousines"

Requirements
Must have
• Must use the colours provided on the PDF uploaded to the portal. The purple = main colour. The red = accent colour.
Nice to have
• Nice to use same font as now for the company name "Marlowin". Font is "Champagne & Limousines". Nice to have some reference to the old logo flower, but only subtle.
Should not have
• Do not use the colour red from our website. Use the colours provided on the colour palette PDF that I uploaded in the portal.

```html
<!DOCTYPE html>
<html lang="en">
<head>
<meta charset="utf-8">
<title>Marlowin Letterhead</title>
<link rel="stylesheet" href="https://fonts.googleapis.com/css2?family=Josefin+Sans:wght@300&family=Quicksand:wght@400;500&display=swap">
<style>
  :root {
    --backdrop: #eeeeee;
    --paper: #ffffff;
    --brand-purple: #3a1a2b;
    --accent-red: #d9452b;
    --ink: #2e2e2e;
    --ink-soft: #4a4a4a;
    --signature-ink: #c9d3f2;
  }
  * { box-sizing: border-box; margin: 0; padding: 0; }
  html, body {
    width: 1200px;
    height: 900px;
    overflow: hidden;
    background: var(--backdrop);
  }
  .canvas {
    width: 1200px;
    height: 900px;
    display: flex;
    align-items: center;
    justify-content: center;
  }
  .letterhead {
    position: relative;
    width: 600px;
    height: 848px;
    background: var(--paper);
    box-shadow: 0 2px 12px rgba(0,0,0,0.08);
    overflow: hidden;
  }
  .edge-band {
    position: absolute;
    top: 0;
    left: 0;
    height: 100%;
  }
  .company-name {
    position: absolute;
    top: 62px;
    right: 58px;
    font-family: "Josefin Sans", sans-serif;
    font-weight: 300;
    font-size: 26px;
    letter-spacing: 0.32em;
    color: var(--ink);
    text-transform: uppercase;
  }
  .letter-content {
    position: absolute;
    top: 200px;
    left: 104px;
    right: 50px;
    display: grid;
    grid-template-columns: 340px 1fr;
    column-gap: 24px;
  }
  .letter-main {
    display: flex;
    flex-direction: column;
  }
  .letter-body {
    font-family: "Quicksand", sans-serif;
    font-weight: 500;
    font-size: 10.4px;
    line-height: 1.38;
    color: var(--ink-soft);
    text-align: justify;
  }
  .letter-body p + p { margin-top: 13px; }
  .sender-address {
    align-self: center;
    margin-top: 90px;
    font-family: "Quicksand", sans-serif;
    font-style: normal;
    font-weight: 500;
    font-size: 9px;
    line-height: 1.45;
    color: var(--ink-soft);
    text-align: right;
    font-variant: small-caps;
  }
  .sign-off {
    margin-top: 18px;
  }
  .signature {
    width: 150px;
    height: 30px;
    background: var(--signature-ink);
    border-radius: 3px;
  }
  .signatory-role {
    margin-top: 4px;
    font-family: "Quicksand", sans-serif;
    font-weight: 500;
    font-size: 11px;
    color: var(--ink);
  }
</style>
</head>
<body>
  <main class="canvas">
    <article class="letterhead">
      <svg class="edge-band" width="36" height="848" viewBox="0 0 36 848" aria-hidden="true">
        <rect x="0" y="0" width="29" height="848" fill="var(--brand-purple)"/>
        <rect x="29" y="0" width="5" height="848" fill="var(--accent-red)"/>
      </svg>

      <h1 class="company-name">Marlowin</h1>

      <div class="letter-content">
        <div class="letter-main">
          <section class="letter-body">
            <p>Letterhead samples are a great way of deciding what kind of letterhead you want to design for you and your company. The internet has a ton of great letterhead samples to browse through. Whether you want something simple, with just a couple lines of text of your business information, or something decorative and stunning, with photos and logos on the top and bottom of the page, it will be easy to find what you want, because there are samples online for basically any type of letterhead you could want.</p>
            <p>Any business could easily benefit from browsing through some letterhead samples, if only to get an idea for what kind of letterhead their company might want. Letterheads are just one of the tools that a business professional could use to help increase their customer base, and to really be memorable to everyone they write a letter to. Letterhead is quite an effective tool for marketing and advertising, but because it's such a simple and well known idea, it is often unfairly overlooked. Make sure you don't make that mistake, and make some letterhead samples of your own today.</p>
            <p>Whether you want to get new customers to remember you and become part of your clientele, or you just want to send out friendly reminders to your existing clients, customizing your own letterhead samples can really help you out. Try out some letterhead samples and you will not regret it, and I'm sure you will add a new tool to your business' arsenal of networking, marketing, and advertising tools.</p>
          </section>

          <footer class="sign-off">
            <div class="signature" role="img" aria-label="Handwritten signature of Elliot Brandwell in blue ink"></div>
            <p class="signatory-role">company director</p>
          </footer>
        </div>

        <address class="sender-address">
          48 Calder Row<br>
          Westbridge, London<br>
          EC2 4QR
        </address>
      </div>
    </article>
  </main>
</body>
</html>
```